TalkBridge - Language Coaching Services

Sleek, innovative, trendy design for Language Coaching business.

TalkBridge is a new UK based company that provides Language Coaching services. We offer highly personalized on-line and face to face language courses. We also impart learning techniques workshops based on the latest neuroscience research for second-language acquisition.

Target Market(s)

Industry/Entity Type

Consulting

Contact Information for Business Card

TalkBridge
ElenaVT@talkbridge-demo.co.uk
TalkBridge-demo.co.uk
London, UK

Font styles to use
Sans Serif

```html
<!DOCTYPE html>
<html lang="en">
<head>
<meta charset="utf-8">
<title>TalkBridge Business Card</title>
<link rel="stylesheet" href="https://fonts.googleapis.com/css2?family=Roboto:wght@300;400;500;700&display=swap">
<style>
  :root {
    --bg: #e9e9e9;
    --card-white: #ffffff;
    --brand-blue: #1b8fc4;
    --brand-deep: #0f6f9f;
    --edge-blue: #19b4ea;
    --text-grey: #5f6266;
    --title-grey: #8c8f93;
    --rule-grey: #d9dadb;
    --back-center: #1cbcef;
    --back-edge: #0a5b88;
  }
  * { margin: 0; padding: 0; box-sizing: border-box; }
  html, body { width: 1125px; height: 1200px; overflow: hidden; }
  body {
    position: relative;
    background: var(--bg);
    font-family: "Roboto", Arial, sans-serif;
  }
  .card {
    position: absolute;
    left: 150px;
    width: 825px;
    height: 470px;
    border-radius: 24px;
    overflow: hidden;
  }
  .card-front {
    top: 98px;
    background: var(--card-white);
  }
  .card-front .edge {
    position: absolute;
    left: 0; right: 0; bottom: 0;
    height: 20px;
    background: linear-gradient(90deg, var(--brand-deep), var(--edge-blue) 50%, var(--brand-deep));
    border-top: 3px solid var(--rule-grey);
  }
  .brand-mark {
    position: absolute;
    left: 96px;
    top: 152px;
    width: 308px;
    text-align: center;
  }
  .brand-circle {
    display: block;
    margin: 0 auto 14px;
    width: 114px;
    height: 114px;
    border-radius: 50%;
    border: 7px solid var(--brand-blue);
  }
  .brand-name {
    font-family: "Roboto", Arial, sans-serif;
    font-weight: 500;
    font-size: 42px;
    letter-spacing: 1px;
    color: var(--brand-blue);
    text-transform: uppercase;
  }
  .divider {
    position: absolute;
    left: 443px;
    top: 152px;
    width: 1px;
    height: 171px;
    background: var(--rule-grey);
  }
  .contact-block {
    position: absolute;
    left: 474px;
    top: 152px;
  }
  .person-name {
    font-size: 31px;
    color: var(--brand-blue);
    font-weight: 300;
    line-height: 1.1;
  }
  .person-name .first { font-weight: 700; }
  .person-title {
    font-size: 20px;
    font-weight: 500;
    color: var(--title-grey);
    margin-top: 2px;
  }
  .contact-list {
    list-style: none;
    margin-top: 20px;
  }
  .contact-list li {
    display: flex;
    align-items: center;
    font-size: 20px;
    color: var(--text-grey);
    height: 27px;
  }
  .contact-list svg {
    width: 18px;
    height: 18px;
    margin-right: 12px;
    fill: var(--brand-blue);
    flex: none;
  }
  .card-back {
    top: 631px;
    background: radial-gradient(ellipse at 50% 45%, var(--back-center) 0%, #1199cf 45%, var(--back-edge) 100%);
  }
  .back-mark {
    position: absolute;
    left: 282px;
    top: 94px;
    width: 260px;
    height: 260px;
    border-radius: 50%;
    border: 13px solid #ffffff;
    display: flex;
    align-items: center;
    justify-content: center;
  }
  .back-mark .brand-name {
    color: #ffffff;
    font-size: 36px;
    text-transform: none;
    letter-spacing: 0;
  }
  .back-url {
    position: absolute;
    left: 0; right: 0;
    top: 400px;
    text-align: center;
    font-size: 19px;
    letter-spacing: 7px;
    color: rgba(255, 255, 255, 0.6);
    font-weight: 400;
  }
</style>
</head>
<body>
  <section class="card card-front">
    <div class="brand-mark">
      <span class="brand-circle"></span>
      <span class="brand-name">TalkBridge</span>
    </div>
    <div class="divider"></div>
    <div class="contact-block">
      <h1 class="person-name"><span class="first">ELENA</span> VIDAL</h1>
      <p class="person-title">CEO/Founder</p>
      <ul class="contact-list">
        <li>
          <svg viewBox="0 0 18 18" aria-hidden="true"><path d="M5 0h8a2 2 0 0 1 2 2v14a2 2 0 0 1-2 2H5a2 2 0 0 1-2-2V2a2 2 0 0 1 2-2zm0 2.5v11h8v-11zM8 15h2v1.5H8z"/></svg>
          020 7946 0321
        </li>
        <li>
          <svg viewBox="0 0 18 18" aria-hidden="true"><path d="M1 4h16v11H1zm1.5 1.5L9 10l6.5-4.5v-0.2h-13z"/></svg>
          ElenaVT@talkbridge-demo.co.uk
        </li>
        <li>
          <svg viewBox="0 0 18 18" aria-hidden="true"><circle cx="9" cy="9" r="8"/><path d="M4 6c2 0 3 1 3 3s2 2 2 4l-2 2c-1-2-3-2-3-4zM10 3c2 0 3 2 5 2l-1 3c-2 0-2-2-4-2z" fill="#ffffff"/></svg>
          www.talkbridge-demo.co.uk
        </li>
      </ul>
    </div>
    <div class="edge"></div>
  </section>

  <section class="card card-back">
    <div class="back-mark">
      <span class="brand-name">TalkBridge</span>
    </div>
    <p class="back-url">www.talkbridge-demo.co.uk</p>
  </section>
</body>
</html>
```